Fiber Arts Workshop: Business Cards & Stationery
Copper Kettle StitchHouse, LLC
Fiber Arts Workshop: Business Cards & Stationery - Hobbies
Creative Brief
Bright & Fun-filled
Marla Penrose
Principal
48 Birchwood Terrace #512 Millbrook, New Jersey 07322
marla.penrose@ckstitchhouse.example
www.ckstitchhouse.example
Fonts - you may use fonts other than those used in the logo if they enhance the design

```html
<!DOCTYPE html>
<html lang="en">
<head>
<meta charset="utf-8">
<title>Copper Kettle StitchHouse — Business Cards</title>
<link rel="stylesheet" href="https://fonts.googleapis.com/css2?family=Open+Sans:wght@400;600&display=swap">
<style>
  :root {
    --backdrop: #e7e4df;
    --card: #ffffff;
    --ink: #444444;
    --ink-soft: #6a6a6a;
    --rule: #b9b9b9;
    --accent-slate: #4f6378;
    --accent-orange: #f08a1c;
    --accent-green: #7aa63a;
    --brand-dot: #e0583a;
  }
  * { box-sizing: border-box; margin: 0; padding: 0; }
  html, body { width: 1200px; height: 720px; overflow: hidden; }
  body {
    background: var(--backdrop);
    font-family: "Open Sans", Arial, sans-serif;
    color: var(--ink);
    position: relative;
  }
  .card {
    position: absolute;
    width: 560px;
    height: 325px;
    background: var(--card);
    box-shadow: 0 2px 8px rgba(0,0,0,0.18);
    overflow: hidden;
  }
  .card--front { left: 320px; top: 22px; }
  .card--orange { left: 14px; top: 376px; }
  .card--green { left: 626px; top: 376px; }

  .brand {
    position: absolute;
    display: flex;
    align-items: center;
    gap: 10px;
  }
  .brand__mark {
    width: 22px; height: 22px;
    border-radius: 50%;
    background: var(--brand-dot);
    flex: none;
  }
  .brand__name {
    font-size: 25px;
    font-weight: 600;
    line-height: 1.05;
    color: var(--ink);
    letter-spacing: -0.3px;
  }
  .card--front .brand { left: 250px; top: 78px; }
  .card--orange .brand, .card--green .brand { left: 70px; top: 70px; }

  .divider {
    position: absolute;
    width: 1px;
    background: var(--rule);
  }
  .card--front .divider { left: 268px; top: 180px; height: 84px; }
  .card--orange .divider { left: 270px; top: 212px; height: 80px; }
  .card--green .divider { left: 262px; top: 212px; height: 80px; }

  .person {
    position: absolute;
    font-size: 11.5px;
    line-height: 17px;
    color: var(--ink-soft);
    white-space: nowrap;
  }
  .card--front .person { right: 304px; top: 186px; text-align: right; }
  .card--orange .person { left: 70px; top: 222px; }
  .card--green .person { right: 310px; top: 222px; text-align: right; }
  .card--orange .person__name,
  .card--orange .person__role { color: var(--accent-orange); }
  .card--green .person__name,
  .card--green .person__role { color: var(--accent-green); }

  .contact {
    position: absolute;
    list-style: none;
    font-size: 11.5px;
    line-height: 20px;
    color: var(--ink-soft);
    white-space: nowrap;
  }
  .card--front .contact { left: 280px; top: 182px; }
  .card--orange .contact { left: 282px; top: 214px; }
  .card--green .contact { left: 274px; top: 214px; }
  .contact__item { display: flex; align-items: center; gap: 7px; }
  .contact__icon { width: 13px; height: 13px; flex: none; }
  .card--front .contact__icon { color: var(--accent-slate); }
  .card--orange .contact__icon { color: var(--accent-orange); }
  .card--green .contact__icon { color: var(--accent-green); }
</style>
</head>
<body>

<svg width="0" height="0" style="position:absolute" aria-hidden="true">
  <defs>
    <symbol id="icon-phone" viewBox="0 0 16 16">
      <circle cx="8" cy="8" r="8" fill="currentColor"/>
      <path d="M5.3 4.2l1.4 0.1 0.6 1.8-0.9 0.7c0.4 1 1.2 1.8 2.2 2.2l0.7-0.9 1.8 0.6 0.1 1.4c-0.3 0.6-0.9 0.9-1.5 0.8-2.5-0.4-4.4-2.3-4.8-4.8-0.1-0.6 0.2-1.2 0.4-1.9z" fill="#fff"/>
    </symbol>
    <symbol id="icon-mail" viewBox="0 0 16 16">
      <circle cx="8" cy="8" r="8" fill="currentColor"/>
      <rect x="4" y="5.3" width="8" height="5.6" rx="0.6" fill="#fff"/>
      <path d="M4.3 5.6L8 8.4l3.7-2.8" fill="none" stroke="currentColor" stroke-width="0.9"/>
    </symbol>
    <symbol id="icon-web" viewBox="0 0 16 16">
      <circle cx="8" cy="8" r="8" fill="currentColor"/>
      <circle cx="8" cy="8" r="4" fill="none" stroke="#fff" stroke-width="1"/>
      <ellipse cx="8" cy="8" rx="1.7" ry="4" fill="none" stroke="#fff" stroke-width="0.9"/>
      <line x1="4" y1="8" x2="12" y2="8" stroke="#fff" stroke-width="0.9"/>
    </symbol>
  </defs>
</svg>

<section class="card card--front">
  <div class="brand">
    <span class="brand__mark"></span>
    <span class="brand__name">Copper Kettle<br>StitchHouse</span>
  </div>
  <div class="person">
    <p class="person__name">Marla Penrose</p>
    <p class="person__role">Principal</p>
    <p>48 Birchwood Terrace #512</p>
    <p>Millbrook, New Jersey 07322</p>
  </div>
  <div class="divider"></div>
  <ul class="contact">
    <li class="contact__item"><svg class="contact__icon"><use href="#icon-phone"/></svg>(973) 555-0148</li>
    <li class="contact__item"><svg class="contact__icon"><use href="#icon-mail"/></svg>marla.penrose@ckstitchhouse.example</li>
    <li class="contact__item"><svg class="contact__icon"><use href="#icon-web"/></svg>www.ckstitchhouse.example</li>
  </ul>
</section>

<section class="card card--orange">
  <div class="brand">
    <span class="brand__mark"></span>
    <span class="brand__name">Copper Kettle<br>StitchHouse</span>
  </div>
  <div class="person">
    <p class="person__name">Marla Penrose</p>
    <p class="person__role">Principal</p>
    <p>48 Birchwood Terrace #512</p>
    <p>Millbrook, New Jersey 07322</p>
  </div>
  <div class="divider"></div>
  <ul class="contact">
    <li class="contact__item"><svg class="contact__icon"><use href="#icon-phone"/></svg>(973) 555-0148</li>
    <li class="contact__item"><svg class="contact__icon"><use href="#icon-mail"/></svg>marla.penrose@ckstitchhouse.example</li>
    <li class="contact__item"><svg class="contact__icon"><use href="#icon-web"/></svg>www.ckstitchhouse.example</li>
  </ul>
</section>

<section class="card card--green">
  <div class="brand">
    <span class="brand__mark"></span>
    <span class="brand__name">Copper Kettle<br>StitchHouse</span>
  </div>
  <div class="person">
    <p class="person__name">Marla Penrose</p>
    <p class="person__role">Principal</p>
    <p>48 Birchwood Terrace #512</p>
    <p>Millbrook, New Jersey 07322</p>
  </div>
  <div class="divider"></div>
  <ul class="contact">
    <li class="contact__item"><svg class="contact__icon"><use href="#icon-phone"/></svg>(973) 555-0148</li>
    <li class="contact__item"><svg class="contact__icon"><use href="#icon-mail"/></svg>marla.penrose@ckstitchhouse.example</li>
    <li class="contact__item"><svg class="contact__icon"><use href="#icon-web"/></svg>www.ckstitchhouse.example</li>
  </ul>
</section>

</body>
</html>
```